Boutique custom software development company needs new business card

Our nearly 20 year old custom software development company would like to better include the fact that we are now providing Bitcoin services. These new services are B2B include education (how to acquire and securely hold Bitcoin) and integrating Bitcoin payments into existing ecommerce sites or other existing systems. Please keep the card clean and simple. Attached is our current design and some other files. vexalon.example

Target Market(s)

businesses owners interested in long term relationship

Industry/Entity Type

Custom software development and Bitcoin

Contact Information for Business Card

Marcus Ellwood, marcus@vexalon.example, vexalon.example, (888) 555-VEXAL

Font styles to use
Other font styles liked:
• monospace

Requirements
Must have
• double-sided
Nice to have
• clean and simple
Should not have
• physical address

```html
<!DOCTYPE html>
<html lang="en">
<head>
<meta charset="utf-8">
<title>Vexalon business card</title>
<link rel="stylesheet" href="https://fonts.googleapis.com/css2?family=Roboto+Mono:wght@400;500&family=Lato:wght@400&display=swap">
<style>
  :root {
    --backdrop: #141414;
    --card: #071433;
    --brand-blue: #3f74bc;
    --tagline-blue: #3f6fb5;
    --accent-orange: #f07f23;
    --ink-light: #f2f4f8;
  }
  * { margin: 0; padding: 0; box-sizing: border-box; }
  html, body { width: 1200px; height: 848px; overflow: hidden; background: var(--backdrop); }
  .canvas { position: relative; width: 1200px; height: 848px; }
  .card {
    position: absolute; left: 281px; width: 616px; height: 334px;
    background: var(--card);
  }
  .card--front { top: 68px; }
  .card--back { top: 445px; }

  .front-brand {
    position: absolute; left: 0; right: 0; top: 0; bottom: 0;
    display: flex; align-items: center; justify-content: center; gap: 14px;
    padding-bottom: 48px;
  }
  .brand-square { width: 40px; height: 40px; background: var(--brand-blue); }
  .front-name {
    font-family: "Roboto Mono", monospace; font-weight: 500;
    font-size: 38px; letter-spacing: 2px; color: var(--ink-light);
  }

  .back-brand {
    position: absolute; left: 30px; top: 26px;
    font-family: "Roboto Mono", monospace; font-weight: 500;
    font-size: 46px; line-height: 46px; letter-spacing: 1px;
    color: var(--accent-orange);
  }
  .tagline {
    position: absolute; left: 40px; top: 76px;
    font-family: "Lato", sans-serif; font-size: 15px; letter-spacing: -0.4px;
    color: var(--tagline-blue);
  }
  .holder-name {
    position: absolute; right: 29px; top: 186px;
    font-family: "Roboto Mono", monospace; font-weight: 500;
    font-size: 23px; color: var(--accent-orange);
  }
  .contact-list {
    position: absolute; left: 30px; top: 250px; list-style: none;
    font-family: "Roboto Mono", monospace; font-size: 14px;
    line-height: 18.7px; color: var(--ink-light);
  }
  .contact-list li { display: flex; align-items: center; gap: 6px; }
  .contact-icon { width: 12px; height: 12px; flex: none; }
</style>
</head>
<body>
<div class="canvas">
  <section class="card card--front">
    <div class="front-brand">
      <span class="brand-square"></span>
      <span class="front-name">VEXALON</span>
    </div>
  </section>

  <section class="card card--back">
    <div class="back-brand">VEXALON</div>
    <div class="tagline">developer of custom applications</div>
    <div class="holder-name">Marcus Ellwood</div>
    <ul class="contact-list">
      <li>
        <svg class="contact-icon" viewBox="0 0 12 12" aria-hidden="true"><path d="M2.5 1 L4.5 1 L5.2 3.4 L4 4.4 Q5 6.8 7.6 8 L8.6 6.8 L11 7.5 L11 9.5 Q10.5 11 9 11 Q1 10 1 3 Q1 1.5 2.5 1 Z" fill="#f07f23"/></svg>
        <span>(888) 555-VEXAL</span>
      </li>
      <li>
        <svg class="contact-icon" viewBox="0 0 12 12" aria-hidden="true"><rect x="0.5" y="2.5" width="11" height="7.5" fill="#f07f23"/><path d="M0.5 2.5 L6 7 L11.5 2.5" fill="none" stroke="#071433" stroke-width="1"/></svg>
        <span>marcus@vexalon.example</span>
      </li>
      <li>
        <svg class="contact-icon" viewBox="0 0 12 12" aria-hidden="true"><g fill="none" stroke="#f07f23" stroke-width="1"><circle cx="6" cy="6" r="5"/><ellipse cx="6" cy="6" rx="2.2" ry="5"/><path d="M1 6 H11 M1.8 3.5 H10.2 M1.8 8.5 H10.2"/></g></svg>
        <span>vexalon.example</span>
      </li>
    </ul>
  </section>
</div>
</body>
</html>
```